RM Tomás Rivera (Business Card)

Hi designers, in this work, I'm looking for an sophisticated stylish, elegant and proffesional personal card. We have a laboratory of pathology automated, with equipments high quality.
In this web the designers, have created my business logo, the name is "RM Tomás Rivera"
In our lab, we principal work is to prepare the biopsies for further diagnostic of diseases like cancer, tumors, etc.
I need that the first face, only having my complete logo (Rm Tomás Rivera, Laboratorio de procesamiento Histologico)
The overleaf, could repeat the same logo, like water logo.
In this face, I need to say: My full data:

Técnico en Anatomía Patológica
Tomás Rivera Ibarra M.P 47203
Av. Paredes Luján 418 - 2do piso - Instituto Marbel.
Córdoba, Argentina
(0351) 154820937
rivera.tomas@correolab.example

with respect the colors of card, use your imagination, the original logo color is violet, I haven't chosen a color base for the card.

attached pictures are examples of cards I like your DESIGN.
Attached too, the original logo to my company.

the size of card are:
horizontal: 9cm
vertical: 5,5cm

any question that you have, not doubt to question me,
Hand to work!

Industry/Entity Type

Laboratory

Requirements
Must have
• designers sophisticated, not simples, like show the images attached

```html
<!DOCTYPE html>
<html lang="es">
<head>
<meta charset="utf-8">
<title>RM Tomás Rivera – Tarjetas</title>
<link rel="stylesheet" href="https://fonts.googleapis.com/css2?family=Comfortaa:wght@400;600&family=Open+Sans:wght@400;600&family=PT+Sans+Narrow&family=Raleway:wght@400;500&display=swap">
<style>
:root{
  --bg:#ecebf0;
  --violet:#6a2c9a;
  --violet-soft:#8a66b8;
  --grey:#707070;
  --grey-dark:#555;
  --card-top:#ffffff;
  --card-bottom:#cdc7e4;
  --lavender:#d6d0ea;
  --white:#ffffff;
}
*{margin:0;padding:0;box-sizing:border-box}
html,body{width:1200px;height:1000px;overflow:hidden}
body{background:var(--bg);position:relative;font-family:"Open Sans",sans-serif}
.card{position:absolute;border-radius:18px;overflow:hidden;
  background:linear-gradient(180deg,var(--card-bottom) 0%,var(--card-top) 35%,var(--card-top) 70%,var(--card-bottom) 100%);
  box-shadow:0 4px 14px rgba(0,0,0,.18)}
.card-front{left:55px;top:362px;width:482px;height:294px}
.card-back-waves{left:603px;top:44px;width:485px;height:297px;
  background:linear-gradient(180deg,#fff 0%,#e3dff1 55%,#fff 100%)}
.card-back-bands{left:600px;top:357px;width:488px;height:297px;
  background:linear-gradient(180deg,#fff 0%,var(--lavender) 45%,var(--lavender) 70%,#fff 100%)}
.card-back-center{left:609px;top:669px;width:483px;height:294px;
  background:linear-gradient(180deg,#fff 0%,var(--lavender) 45%,var(--lavender) 75%,#fff 100%)}
.abs{position:absolute}
.brand{font-family:"Raleway",sans-serif;font-weight:500;color:var(--violet);white-space:nowrap;display:flex;align-items:center;gap:12px}
.brand-dot{width:14px;height:14px;border-radius:50%;background:var(--violet)}
.tagline{font-family:"PT Sans Narrow",sans-serif;color:var(--grey);white-space:nowrap}
.role{font-family:"Comfortaa",sans-serif;color:var(--grey);white-space:nowrap}
.contact{font-family:"Open Sans",sans-serif;color:var(--violet);white-space:nowrap;font-size:13px}
.contact small{font-size:7px;margin-left:5px}
.email{font-family:"Comfortaa",sans-serif;font-weight:600;color:var(--violet);white-space:nowrap}
.icon{width:14px;height:14px}
.waves-area{left:0;top:0;width:485px;height:297px;
  background:linear-gradient(170deg,rgba(255,255,255,0) 10%,rgba(150,120,200,.28) 45%,rgba(255,255,255,0) 80%)}
.band-line{position:absolute;left:0;width:100%;height:6px;background:var(--white)}
</style>
</head>
<body>

<section class="card card-front">
  <div class="abs brand" style="left:0;width:482px;justify-content:center;top:128px;font-size:30px">
    <span class="brand-dot"></span>RM Tomás Rivera
  </div>
  <div class="abs" style="left:70px;top:184px;width:336px;height:2px;background:var(--grey)"></div>
  <div class="abs tagline" style="left:0;width:482px;text-align:center;top:188px;font-size:26px">LABORATORIO DE PROCESAMIENTO HISTOLOGICO</div>
</section>

<section class="card card-back-waves">
  <div class="abs waves-area" role="img" aria-label="Haz de líneas onduladas violetas cruzando la tarjeta"></div>
  <div class="abs brand" style="left:0;width:485px;justify-content:center;top:68px;font-size:22px">
    <span class="brand-dot" style="width:10px;height:10px"></span>RM Tomás Rivera
  </div>
  <div class="abs role" style="left:0;width:485px;text-align:center;top:96px;font-size:11px">Técnico en Anatomía Patológica</div>
  <svg class="abs icon" style="left:50px;top:188px" viewBox="0 0 14 14"><rect x="3" y="1" width="8" height="12" rx="1.5" fill="var(--violet-soft)"/><rect x="4.5" y="3" width="5" height="4" fill="#fff"/></svg>
  <div class="abs contact" style="left:86px;top:186px">(0351) 154820937</div>
  <svg class="abs icon" style="left:50px;top:216px" viewBox="0 0 14 14"><circle cx="7" cy="7" r="6" fill="var(--violet-soft)"/><path d="M1 7h12M7 1v12" stroke="#fff" stroke-width="1"/></svg>
  <div class="abs email" style="left:86px;top:213px;font-size:15px">rivera.tomas@correolab.example</div>
  <svg class="abs icon" style="left:50px;top:245px" viewBox="0 0 14 14"><path d="M7 1L1 7h2v6h8V7h2z" fill="var(--violet-soft)"/></svg>
  <div class="abs contact" style="left:86px;top:245px;font-size:10px">Av. Paredes Luján 418 - 2do piso - Instituto Marbel. <small>Córdoba, Argentina</small></div>
</section>

<section class="card card-back-bands">
  <div class="band-line" style="top:123px"></div>
  <div class="band-line" style="top:252px"></div>
  <div class="abs brand" style="left:22px;top:70px;font-size:18px"><span class="brand-dot" style="width:9px;height:9px"></span>RM Tomás Rivera</div>
  <div class="abs" style="left:280px;top:76px;font-size:11px;color:var(--grey);white-space:nowrap">TECNICO EN ANATOMIA PATOLOGICA</div>
  <div class="abs email" style="left:0;width:488px;text-align:center;top:143px;font-size:14px">rivera.tomas@correolab.example</div>
  <svg class="abs icon" style="left:172px;top:186px" viewBox="0 0 14 14"><rect x="3" y="1" width="8" height="12" rx="1.5" fill="var(--violet-soft)"/><rect x="4.5" y="3" width="5" height="4" fill="#fff"/></svg>
  <div class="abs contact" style="left:208px;top:185px">(0351) 154820937</div>
  <svg class="abs icon" style="left:363px;top:177px" viewBox="0 0 14 14"><circle cx="7" cy="7" r="6" fill="var(--violet-soft)"/><path d="M1 7h12M7 1v12" stroke="#fff" stroke-width="1"/></svg>
  <svg class="abs icon" style="left:122px;top:202px" viewBox="0 0 14 14"><path d="M7 1L1 7h2v6h8V7h2z" fill="var(--violet-soft)"/></svg>
  <div class="abs contact" style="left:0;width:488px;text-align:center;top:223px;font-size:10px">Av. Paredes Luján 418 - 2do piso - Instituto Marbel.</div>
  <div class="abs contact" style="left:355px;top:239px;font-size:7px">Córdoba, Argentina</div>
</section>

<section class="card card-back-center">
  <div class="abs role" style="left:0;width:483px;text-align:center;top:20px;font-size:13px">Técnico en Anatomía Patológica</div>
  <div class="abs email" style="left:0;width:483px;text-align:center;top:42px;font-size:27px">Tomás Rivera Ibarra</div>
  <div class="abs" style="left:398px;top:78px;font-size:6px;color:var(--grey-dark);white-space:nowrap">M.P 47203</div>
  <div class="abs email" style="left:0;width:483px;text-align:center;top:143px;font-size:18px;font-weight:400">rivera.tomas@correolab.example</div>
  <svg class="abs icon" style="left:54px;top:252px" viewBox="0 0 14 14"><rect x="3" y="1" width="8" height="12" rx="1.5" fill="var(--violet-soft)"/><rect x="4.5" y="3" width="5" height="4" fill="#fff"/></svg>
  <div class="abs contact" style="left:0;width:483px;text-align:center;top:249px;font-size:16px;color:var(--grey-dark)">(0351) 154820937</div>
  <svg class="abs icon" style="left:54px;top:272px" viewBox="0 0 14 14"><path d="M7 1L1 7h2v6h8V7h2z" fill="var(--violet)"/></svg>
  <div class="abs contact" style="left:84px;top:274px;font-size:10px;color:var(--grey-dark)">Av. Paredes Luján 418 - 2do piso - Instituto Marbel. <small>Córdoba, Argentina</small></div>
</section>

</body>
</html>
```